FC Quintel and Canvas flyer for our communications

1. Introduction:
FC Quintel is a dynamic and passionate amateur football club, consisting of approximately 600 members. We are looking to create a versatile Canvas poster template that can be used for various purposes, including promoting matches, announcing special events such as gala dinners or football tournaments, as well as for promoting our recruitment activities to schools.

2. Objective:
The aim of this project is to create an attractive and professional poster template that reflects the spirit of FC Quintel, while being easily adaptable for different types of communications. We want the template to convey the excitement, energy, and sense of belonging to our club, highlighting our primary colors (red and blue) as well as our logo.

3. Key Elements of the Template:
The template should include the following elements clearly and organized:

FC Quintel Logo: Ensure the club logo is displayed or even better a strong visual identification of the key element of the logo are easily recognizable on the poster.

Club Colors: Use the main FC Quintel colors (red and blue) dominantly to create a strong visual identification with the club.

Editable Spaces: Provide dedicated and editable spaces to include event-specific information such as date, time, venue, sponsor logos, and any other relevant content.

4. Layout and Composition:
The layout should be clean, balanced, and appealing, with clear visual hierarchy for each element. Ensure the template is flexible enough to accommodate different types of content while maintaining a consistent look.

5. Variants Options:
We would like to have different template variants, with slightly different layouts for match posters, special event announcements, and recruitment advertising posters. However, the core visual and key elements will remain the same.

6. Tone and Style:
The tone of the poster should be energetic, enthusiastic, and professional. Avoid overly cluttered elements and focus on simplicity and readability.

7. Format and Deliverables:
The template should be created in digital format (Canvas), with dimensions suitable for printing (e.g., A3 size) while also being compatible with digital media. Provide the template in an editable format (e.g., PSD or AI) as well as in final print-ready formats (PDF, JPG, PNG).

Target Market(s)

Fooball players, members of the club, parents of the kids of the clubs, sponsors

Industry/Entity Type

Football (soccer)

Font styles to use
Sans Serif

Colors
0054AA
0677BA
7BADD7
CADEEF
E8F1F8
0094D4
00A9DD
6FCCEA
C7EBF8
E9F6FB
EB3D1F
EC4F4E
F09395
F8D3D4
FCEDEE

Requirements
Must have
• Colors of the club

```html
<!DOCTYPE html>
<html lang="en">
<head>
<meta charset="utf-8">
<title>FC Quintel – Poster Templates</title>
<link href="https://fonts.googleapis.com/css2?family=Alfa+Slab+One&family=Roboto+Condensed:wght@400;700&family=Great+Vibes&display=swap" rel="stylesheet">
<style>
:root{
  --blue:#0088CC;
  --blue-deep:#0677BA;
  --red:#ED2038;
  --red-deep:#B50F22;
  --ink:#231F20;
  --grey:#8C8C8C;
  --grey-light:#C8C8C8;
  --paper-a:#E4E5E6;
  --paper-b:#F5F5F5;
  --white:#FFFFFF;
}
*{margin:0;padding:0;box-sizing:border-box}
html,body{width:849px;height:1200px;overflow:hidden;background:var(--white)}
body{position:relative;font-family:"Roboto Condensed",sans-serif;color:var(--ink)}
.panel{position:absolute;overflow:hidden;background:linear-gradient(135deg,var(--paper-a),var(--paper-b) 50%,var(--paper-a))}
.panel>*{position:absolute}
.bands{left:0;top:0;width:100%;height:100%}
.club-name{font-family:"Roboto Condensed",sans-serif;font-weight:700;line-height:.95;text-align:center}
.slab{font-family:"Alfa Slab One",serif;font-weight:400;line-height:1;white-space:nowrap;text-align:center;text-shadow:1px 1px 0 var(--white),-1px -1px 0 var(--white),1px -1px 0 var(--white),-1px 1px 0 var(--white),3px 3px 4px rgba(0,0,0,.3)}
.red{color:var(--red)}
.blue{color:var(--blue)}
.ink{color:var(--ink)}
.body-copy{font-size:7px;line-height:1.4;text-align:center;font-weight:400}
.placeholder{background:var(--grey);color:var(--grey-light);display:flex;align-items:center;justify-content:center;font-family:"Roboto Condensed",sans-serif}
.chip{background:var(--grey-light);color:var(--white);font-size:5px;font-weight:700;display:flex;align-items:center;justify-content:center;border:1px solid var(--white)}
.sponsor{background:var(--grey);color:#A9A9A9;font-size:4.5px;display:flex;align-items:center;justify-content:center}
.sponsor-outline{background:var(--white);border:1px solid var(--ink);font-size:2.5px;display:flex;align-items:center;justify-content:center}
.contacts{color:var(--white);display:grid;grid-auto-flow:row}
.contacts span{display:flex;align-items:center;gap:.5em;white-space:nowrap}
.contacts svg{width:1.1em;height:1.1em;flex:none}
</style>
</head>
<body>

<svg width="0" height="0" style="position:absolute">
  <defs>
    <symbol id="ic-mail" viewBox="0 0 10 10"><rect width="10" height="10" rx="1" fill="#fff"/><path d="M2 3h6v4H2z M2 3l3 2.3L8 3" fill="none" stroke="#ED2038" stroke-width=".8"/></symbol>
    <symbol id="ic-phone" viewBox="0 0 10 10"><rect width="10" height="10" rx="1" fill="#fff"/><path d="M3 2l1.3 1.6-.7.9c.5 1 1.2 1.7 2.2 2.2l.9-.7L8 7.3 7.2 8.3C4.7 8 2 5.3 1.8 2.8z" fill="#ED2038"/></symbol>
    <symbol id="ic-pin" viewBox="0 0 10 10"><rect width="10" height="10" rx="1" fill="#fff"/><path d="M5 8.5S2.5 5.8 2.5 4.2a2.5 2.5 0 0 1 5 0C7.5 5.8 5 8.5 5 8.5z" fill="#ED2038"/><circle cx="5" cy="4.2" r=".9" fill="#fff"/></symbol>
    <symbol id="ic-web" viewBox="0 0 10 10"><rect width="10" height="10" rx="1" fill="#fff"/><path d="M3.5 2.5l4 2.2-1.8.5 1.2 2-1 .5-1.1-2-1.3 1.2z" fill="#ED2038"/></symbol>
  </defs>
</svg>

<!-- Banner -->
<section class="panel banner" style="left:56px;top:59px;width:737px;height:182px">
  <svg class="bands" viewBox="0 0 737 182" preserveAspectRatio="none" aria-hidden="true">
    <polygon points="0,0 165,0 0,138" fill="var(--blue)"/>
    <polygon points="0,150 200,10 205,12 0,160" fill="var(--blue)"/>
    <polygon points="170,40 228,0 253,0" fill="var(--red)"/>
    <polygon points="532,182 737,182 737,62" fill="var(--red)"/>
    <polygon points="511,182 530,182 737,48 737,42" fill="var(--blue)"/>
    <polygon points="737,50 737,58 600,145" fill="var(--red)"/>
  </svg>
  <div class="club-name" style="left:10px;top:40px;width:80px;font-size:20px;color:var(--white)">FC<br>Quintel</div>
  <div class="slab red" style="left:160px;top:18px;width:230px;font-size:44px">DUMMY</div>
  <div class="slab red" style="left:160px;top:68px;width:230px;font-size:44px">TEXT</div>
  <div class="slab blue" style="left:405px;top:20px;width:300px;font-size:35px">LOREM IPSUM</div>
  <p class="body-copy" style="left:450px;top:68px;width:212px">Lorem Ipsum is simply dummy text of the printing and typesetting industry. Lorem Ipsum has been the industry's standard dummy text ever since the 1500s, when an unknown printer took a galley of type and scrambled it to make a type specimen book. It has survived not only five centuries, but also the leap into electronic typesetting.</p>
  <div class="chip" style="left:164px;top:139px;width:46px;height:24px">content</div>
  <div class="chip" style="left:225px;top:139px;width:46px;height:24px">content</div>
  <div class="chip" style="left:286px;top:139px;width:46px;height:24px">content</div>
  <div class="chip" style="left:347px;top:139px;width:46px;height:24px">content</div>
  <div class="chip" style="left:408px;top:139px;width:46px;height:24px">content</div>
  <div class="chip" style="left:470px;top:139px;width:46px;height:24px">content</div>
  <div class="contacts" style="left:595px;top:154px;font-size:4.6px;grid-template-columns:70px 70px;row-gap:4px">
    <span><svg><use href="#ic-mail"/></svg>hello@quintelmail.org</span>
    <span><svg><use href="#ic-pin"/></svg>12 Meadow Lane - Valdoria</span>
    <span><svg><use href="#ic-phone"/></svg>010 555 0147</span>
    <span><svg><use href="#ic-web"/></svg>www.quintelclub.org</span>
  </div>
</section>

<!-- Tall event poster -->
<section class="panel poster-tall" style="left:56px;top:262px;width:355px;height:879px">
  <svg class="bands" viewBox="0 0 355 879" preserveAspectRatio="none" aria-hidden="true">
    <polygon points="0,0 312,0 0,218" fill="var(--blue)"/>
    <polygon points="0,228 190,95 195,96 0,238" fill="var(--blue)"/>
    <polygon points="160,128 318,0 355,0" fill="var(--red)"/>
    <polygon points="36,879 355,879 355,635" fill="var(--red)"/>
    <polygon points="355,600 355,612 125,782" fill="var(--red)"/>
    <polygon points="0,879 14,879 190,750 186,748" fill="var(--blue)"/>
  </svg>
  <div class="club-name" style="left:18px;top:70px;width:100px;font-size:28px;color:var(--white)">FC<br>Quintel</div>
  <div class="slab red" style="left:180px;top:44px;width:140px;font-size:29px">DUMMY</div>
  <div class="slab red" style="left:180px;top:89px;width:140px;font-size:29px">TEXT</div>
  <div class="slab blue" style="left:180px;top:134px;width:140px;font-size:29px">LOREM</div>
  <div class="slab blue" style="left:180px;top:179px;width:140px;font-size:29px">IPSUM</div>
  <h2 class="slab ink" style="left:0;top:242px;width:355px;font-size:22px">HEDLINE LOREM</h2>
  <div class="placeholder" role="img" aria-label="Main event photo" style="left:18px;top:271px;width:319px;height:128px;font-size:56px">image</div>
  <h2 class="slab ink" style="left:0;top:418px;width:355px;font-size:22px">HEDLINE LOREM</h2>
  <div class="placeholder" role="img" aria-label="Match photo" style="left:18px;top:451px;width:99px;height:107px;font-size:20px">image</div>
  <div class="placeholder" role="img" aria-label="Match photo" style="left:128px;top:451px;width:99px;height:107px;font-size:20px">image</div>
  <div class="placeholder" role="img" aria-label="Match photo" style="left:238px;top:451px;width:99px;height:107px;font-size:20px">image</div>
  <h2 class="slab ink" style="left:0;top:588px;width:355px;font-size:22px">HEDLINE LOREM</h2>
  <div class="placeholder" role="img" aria-label="Team photo" style="left:18px;top:621px;width:153px;height:162px;font-size:28px">image</div>
  <div class="placeholder" role="img" aria-label="Team photo" style="left:184px;top:621px;width:153px;height:162px;font-size:28px">image</div>
  <div class="contacts" style="left:120px;top:839px;font-size:8px;grid-template-columns:116px 110px;row-gap:6px">
    <span><svg><use href="#ic-mail"/></svg>hello@quintelmail.org</span>
    <span><svg><use href="#ic-pin"/></svg>12 Meadow Lane - Valdoria</span>
    <span><svg><use href="#ic-phone"/></svg>010 555 0147</span>
    <span><svg><use href="#ic-web"/></svg>www.quintelclub.org</span>
  </div>
</section>

<!-- Match poster -->
<section class="panel poster-match" style="left:438px;top:262px;width:355px;height:502px">
  <svg class="bands" viewBox="0 0 355 502" preserveAspectRatio="none" aria-hidden="true">
    <polygon points="0,0 180,0 0,127" fill="var(--blue)"/>
    <polygon points="0,137 145,35 148,37 0,143" fill="var(--blue)"/>
    <polygon points="150,45 205,0 226,0" fill="var(--red)"/>
    <polygon points="150,502 355,502 355,380" fill="var(--red)"/>
    <polygon points="355,360 355,368 270,420" fill="var(--red)"/>
    <polygon points="128,502 140,502 250,428 246,427" fill="var(--blue)"/>
  </svg>
  <div class="club-name" style="left:137px;top:30px;width:80px;font-size:20px;color:var(--ink)">FC<br>Quintel</div>
  <h1 class="slab ink" style="left:0;top:99px;width:355px;font-size:36px">HEADLINE</h1>
  <div class="slab" style="left:0;top:139px;width:355px;font-size:36px"><span class="blue">LOREM</span> <span class="red">IPSUM</span></div>
  <p class="body-copy" style="left:28px;top:195px;width:136px">Lorem Ipsum is simply dummy text of the printing and typesetting industry. Lorem Ipsum has been the industry's standard dummy text ever since the 1500s, when an unknown printer took a galley of type and scrambled it to make a type specimen book. It has survived not only five centuries, but also the leap into electronic typesetting,</p>
  <div style="left:177px;top:195px;width:1px;height:92px;background:var(--ink)"></div>
  <p class="body-copy" style="left:190px;top:195px;width:136px"><b>Lorem Ipsum</b> is simply dummy text of the printing and typesetting industry. Lorem Ipsum has been the industry's standard dummy text ever since the 1500s, when an unknown printer took a galley of type and scrambled it to make a type specimen book. It has survived not only five centuries, but also the leap into electronic typesetting,</p>
  <div style="left:0;top:288px;width:355px;text-align:center;font-family:'Great Vibes',cursive;font-size:54px;color:var(--blue-deep)">Dummy text</div>
  <p class="body-copy" style="left:26px;top:361px;width:302px;height:36px;background:var(--white);border-radius:5px;padding:4px 10px;font-size:6.3px">Lorem Ipsum is simply dummy text of the printing and typesetting industry. Lorem Ipsum has been the industry's standard dummy text ever since the 1500s, when an unknown printer took a galley of type and scrambled it to make a type specimen book. It has survived not only five centuries, but also the leap into</p>
  <div style="left:87px;top:415px;font-size:12px;font-weight:700">Sponcored by:</div>
  <div class="sponsor" style="left:22px;top:441px;width:30px;height:15px">Sponsor</div>
  <div class="sponsor" style="left:63px;top:441px;width:30px;height:15px">Sponsor</div>
  <div class="sponsor" style="left:104px;top:441px;width:30px;height:15px">Sponsor</div>
  <div class="sponsor" style="left:147px;top:442px;width:30px;height:15px">Sponsor</div>
  <div class="sponsor" style="left:25px;top:464px;width:30px;height:15px">Sponsor</div>
  <div class="sponsor" style="left:65px;top:464px;width:30px;height:15px">Sponsor</div>
  <div class="sponsor" style="left:106px;top:464px;width:30px;height:15px">Sponsor</div>
  <div class="contacts" style="left:262px;top:445px;font-size:6.3px;row-gap:4px">
    <span><svg><use href="#ic-mail"/></svg>hello@quintelmail.org</span>
    <span><svg><use href="#ic-phone"/></svg>010 555 0147</span>
    <span><svg><use href="#ic-pin"/></svg>12 Meadow Lane - Valdoria</span>
    <span><svg><use href="#ic-web"/></svg>www.quintelclub.org</span>
  </div>
</section>

<!-- Recruitment poster -->
<section class="panel poster-recruit" style="left:438px;top:787px;width:355px;height:355px">
  <svg class="bands" viewBox="0 0 355 355" preserveAspectRatio="none" aria-hidden="true">
    <polygon points="0,0 170,0 0,92" fill="var(--blue)"/>
    <polygon points="0,102 140,25 143,27 0,108" fill="var(--blue)"/>
    <polygon points="140,35 175,0 195,0" fill="var(--red)"/>
    <polygon points="205,355 355,355 355,266" fill="var(--red)"/>
    <polygon points="355,250 355,256 245,320" fill="var(--red)"/>
    <polygon points="186,355 196,355 280,302 277,301" fill="var(--blue)"/>
  </svg>
  <div class="club-name" style="left:136px;top:28px;width:80px;font-size:20px;color:var(--ink)">FC<br>Quintel</div>
  <h1 class="slab red" style="left:0;top:104px;width:355px;font-size:40px">HEADLINE</h1>
  <p class="body-copy" style="left:20px;top:161px;width:315px;font-size:6.3px">Lorem Ipsum is simply dummy text of the printing and typesetting industry. Lorem Ipsum has been the industry's standard dummy text ever since the 1500s, when an unknown printer took a galley of type and scrambled it to make a type specimen book. It has survived not only five centuries, but also the leap into electronic typesetting,</p>
  <div class="slab ink" style="left:33px;top:218px;width:130px;font-size:22px">LOREM</div>
  <div class="slab ink" style="left:188px;top:218px;width:130px;font-size:22px">IPSUM</div>
  <p class="body-copy" style="left:33px;top:252px;width:130px;font-size:4.4px">Lorem Ipsum is simply dummy text of the printing and typesetting industry. Lorem Ipsum has been the industry's standard dummy text ever since the 1500s, when an unknown printer took a galley of type and scrambled it to make a type specimen book. It has survived not only five centuries, but also the leap into electronic typesetting,</p>
  <p class="body-copy" style="left:188px;top:252px;width:130px;font-size:4.4px">Lorem Ipsum is simply dummy text of the printing and typesetting industry. Lorem Ipsum has been the industry's standard dummy text ever since the 1500s, when an unknown printer took a galley of type and scrambled it to make a type specimen book. It has survived not only five centuries, but also the leap into electronic</p>
  <div style="left:19px;top:322px;font-size:8px">Sponcored By:</div>
  <div class="sponsor-outline" style="left:78px;top:311px;width:17px;height:13px">Sponsor</div>
  <div class="sponsor-outline" style="left:108px;top:311px;width:17px;height:13px">Sponsor</div>
  <div class="sponsor-outline" style="left:137px;top:311px;width:17px;height:13px">Sponsor</div>
  <div class="sponsor-outline" style="left:166px;top:311px;width:17px;height:13px">Sponsor</div>
  <div class="sponsor-outline" style="left:78px;top:330px;width:17px;height:13px">Sponsor</div>
  <div class="sponsor-outline" style="left:108px;top:330px;width:17px;height:13px">Sponsor</div>
  <div class="sponsor-outline" style="left:137px;top:330px;width:17px;height:13px">Sponsor</div>
  <div class="sponsor-outline" style="left:166px;top:330px;width:17px;height:13px">Sponsor</div>
  <div class="contacts" style="left:244px;top:334px;font-size:3.6px;grid-template-columns:54px 54px;row-gap:3px">
    <span><svg><use href="#ic-mail"/></svg>hello@quintelmail.org</span>
    <span><svg><use href="#ic-pin"/></svg>12 Meadow Lane - Valdoria</span>
    <span><svg><use href="#ic-phone"/></svg>010 555 0147</span>
    <span><svg><use href="#ic-web"/></svg>www.quintelclub.org</span>
  </div>
</section>

</body>
</html>
```